Business Card for a Wedding Films Business

We require a business card design for our business 'Lewis Marrow Wedding Films'. The logo needs to look classy and high end.

Target Market(s)

Wedding Couples

Contact Information for Business Card

Lewis Marrow Wedding Films
07312 605 227
films@lewismarrowreels.com
www.lewismarrowreels.com

Facebook: @lewismarrowweddingfilms
Instagram: @lewismarrowfilms

Font styles to use
Sans Serif

Requirements
Must have
• Social media icons - Facebook and Instagram

```html
<!DOCTYPE html>
<html lang="en">
<head>
<meta charset="utf-8">
<title>Lewis Marrow Wedding Films – Business Card</title>
<link href="https://fonts.googleapis.com/css2?family=Jost:wght@400;500&display=swap" rel="stylesheet">
<style>
  :root {
    --backdrop: #e9e4dc;
    --card-clear: #eeeeec;
    --card-edge: #d6d6d2;
    --ink: #151515;
    --band: #0d0c0b;
    --band-text: #e8e6e2;
    --band-warm: #d8c2ad;
    --icon: #bdb8b0;
  }
  * { box-sizing: border-box; margin: 0; padding: 0; }
  html, body {
    width: 1200px; height: 887px; overflow: hidden;
    background: var(--backdrop);
    font-family: "Jost", "Futura", sans-serif;
  }
  .card {
    position: absolute; left: 100px; top: 163px;
    width: 1000px; height: 560px;
    border-radius: 30px; overflow: hidden;
    background: var(--card-clear);
    border: 2px solid var(--card-edge);
  }
  .brand {
    position: absolute; left: 54px; top: 92px; width: 340px;
    text-align: center; color: var(--ink);
  }
  .brand-mark {
    display: block; width: 22px; height: 22px; margin: 0 auto 22px;
    background: var(--ink);
  }
  .brand-name {
    font-size: 30px; font-weight: 500; letter-spacing: 6px; line-height: 1;
  }
  .brand-tag {
    margin-top: 10px; font-size: 15px; font-weight: 500; letter-spacing: 6px;
  }
  .person {
    position: absolute; right: 72px; top: 180px; text-align: right; color: var(--ink);
  }
  .person-name { font-size: 35px; font-weight: 500; letter-spacing: 1px; line-height: 1; }
  .person-role { margin-top: 6px; font-size: 21px; }
  .person-rule {
    position: absolute; right: 30px; top: 182px; width: 10px; height: 55px; background: var(--ink);
  }
  .band {
    position: absolute; left: 0; right: 0; top: 306px; bottom: 0; background: var(--band);
  }
  .contacts {
    position: absolute; left: 46px; top: 38px; list-style: none;
  }
  .contacts li {
    display: flex; align-items: center; height: 32px;
    font-size: 23px; color: var(--band-text);
  }
  .contacts li.gap { margin-top: 12px; }
  .contacts li.warm { color: var(--band-warm); }
  .contacts .icon { width: 14px; height: 14px; margin-right: 12px; flex: none; }
  .contacts .square { background: var(--icon); }
  .band-brand {
    position: absolute; right: 60px; bottom: 40px;
    font-size: 34px; font-weight: 500; letter-spacing: 6px; color: var(--band-text);
  }
</style>
</head>
<body>
  <div class="card">
    <div class="brand">
      <span class="brand-mark"></span>
      <div class="brand-name">LEWIS MARROW</div>
      <div class="brand-tag">WEDDING FILMS</div>
    </div>

    <div class="person">
      <div class="person-name">DANIEL HART</div>
      <div class="person-role">Director</div>
    </div>
    <div class="person-rule"></div>

    <div class="band">
      <ul class="contacts">
        <li><span class="icon square"></span>/lewismarrowweddingfilms</li>
        <li><span class="icon square"></span>@lewismarrowfilms</li>
        <li class="gap warm">
          <svg class="icon" viewBox="0 0 16 16"><path d="M4 1l3 3-2 2c1 2 3 4 5 5l2-2 3 3-2 3C7 15 1 9 1 3z" fill="var(--icon)"/></svg>
          07312 605 227</li>
        <li class="warm">
          <svg class="icon" viewBox="0 0 16 16"><rect x="1" y="3" width="14" height="10" fill="none" stroke="var(--icon)" stroke-width="1.5"/><path d="M1 3l7 6 7-6" fill="none" stroke="var(--icon)" stroke-width="1.5"/></svg>
          films@lewismarrowreels.com</li>
        <li class="warm">
          <svg class="icon" viewBox="0 0 16 16"><circle cx="8" cy="8" r="6.5" fill="none" stroke="var(--icon)" stroke-width="1.4"/><ellipse cx="8" cy="8" rx="3" ry="6.5" fill="none" stroke="var(--icon)" stroke-width="1.2"/><path d="M1.5 8h13" stroke="var(--icon)" stroke-width="1.2"/></svg>
          www.lewismarrowreels.com</li>
      </ul>
      <div class="band-brand">LEWIS MARROW</div>
    </div>
  </div>
</body>
</html>
```